Business Card

We need some ideas for corporate business cards. I'm interested in a double sided card, with one side featuring our corporate logo, the other side with employee information.

Corporate colors, logo etc. available at www.brivalo.com

Industry/Entity Type

Business

Requirements
Must have
• The "Brivalo" logo with stylized "O"

Nice to have
• Preferred font is calibri

```html
<!DOCTYPE html>
<html lang="en">
<head>
<meta charset="utf-8">
<title>Brivalo Business Card</title>
<link rel="stylesheet" href="https://fonts.googleapis.com/css2?family=Carlito:wght@400;700&display=swap">
<style>
  :root {
    --brand-blue: #4a6291;
    --paper: #ffffff;
    --ink: #1e1e1e;
    --edge: #222222;
  }
  * { box-sizing: border-box; margin: 0; padding: 0; }
  html, body {
    width: 1200px;
    height: 848px;
    overflow: hidden;
    background: var(--paper);
    font-family: "Carlito", "Calibri", sans-serif;
    color: var(--ink);
  }
  .canvas { position: relative; width: 1200px; height: 848px; }

  .card {
    position: absolute;
    left: 222px;
    width: 713px;
    border: 2px solid var(--edge);
    background: var(--paper);
    overflow: hidden;
  }
  .card--front { top: 12px; height: 390px; }
  .card--back { top: 422px; height: 389px; }

  .band { position: absolute; left: 0; right: 0; background: var(--brand-blue); }
  .band--top { top: 61px; height: 28px; }
  .band--main { top: 110px; height: 171px; }
  .band--bottom { top: 299px; height: 28px; }

  .wordmark {
    color: var(--paper);
    font-weight: 700;
    text-transform: uppercase;
    display: flex;
    align-items: center;
    white-space: nowrap;
  }
  .wordmark__square { background: var(--paper); flex: none; }

  .wordmark--large {
    position: absolute;
    left: 0; right: 0; top: 0; bottom: 0;
    justify-content: center;
    font-size: 138px;
    letter-spacing: 8px;
    line-height: 1;
  }
  .wordmark--large .wordmark__square { width: 56px; height: 56px; margin-right: 22px; }

  .header {
    position: absolute;
    left: 1px; right: 1px; top: 9px;
    height: 96px;
    background: var(--brand-blue);
  }
  .wordmark--small {
    position: absolute;
    left: 11px; top: 25px;
    font-size: 32px;
    letter-spacing: 3px;
    line-height: 1;
  }
  .wordmark--small .wordmark__square { width: 13px; height: 13px; margin-right: 8px; }

  .employee {
    position: absolute;
    right: 6px; top: 2px;
    width: 250px;
    text-align: center;
    color: var(--paper);
    line-height: 1.1;
  }
  .employee__name { font-size: 30px; font-weight: 700; letter-spacing: 0.5px; }
  .employee__title { font-size: 22px; text-transform: uppercase; margin-top: 6px; }
  .employee__email { font-size: 21px; margin-top: 3px; }

  .address {
    position: absolute;
    left: 0; right: 0; top: 112px;
    text-align: center;
    font-style: normal;
    font-size: 25px;
    line-height: 35.5px;
  }

  .contact {
    position: absolute;
    top: 302px;
    font-size: 25px;
    line-height: 35px;
  }
  .contact--phones { left: 28px; }
  .contact--general { right: 30px; }
</style>
</head>
<body>
<main class="canvas">

  <section class="card card--front" aria-label="Card front">
    <div class="band band--top"></div>
    <div class="band band--main">
      <div class="wordmark wordmark--large">
        <span class="wordmark__square" aria-hidden="true"></span>Brivalo
      </div>
    </div>
    <div class="band band--bottom"></div>
  </section>

  <section class="card card--back" aria-label="Card back">
    <header class="header">
      <div class="wordmark wordmark--small">
        <span class="wordmark__square" aria-hidden="true"></span>Brivalo
      </div>
      <div class="employee">
        <p class="employee__name">DANIEL HARTE</p>
        <p class="employee__title">Account Manager</p>
        <p class="employee__email">daniel.harte@brivalo.com</p>
      </div>
    </header>

    <address class="address">
      14 Larkfield Row,<br>
      Glenmore Business Park,<br>
      Dublin 14<br>
      Dublin, DB<br>
      Ireland
    </address>

    <div class="contact contact--phones">
      <p>Tel: +353 1 555 0142</p>
      <p>Fax: +353 1 555 0178</p>
    </div>
    <div class="contact contact--general">
      <p>info@brivalo.com</p>
    </div>
  </section>

</main>
</body>
</html>
```